New IPv6 service needs a Web Design

We're launching a brand new service which is designed to connect the current Internet Protocol (IPv4) to the new Internet Protocol (IPv6).
The logo can be found at http://www.brelvo-link.example
We're looking for a clean and simple design, nothing super-fancy. There has to be room for some menu items and a place where people can login (so an e-mail and password box and login button, which must be replaced by the username and a logout button when the user is logged in).
We need a place for a rotating billboard (see http://qa.zx for an example) or a video.
Designs that incorporate IPv4 - IPv6 elements (images with interconnecting networks, videos doing the same) will be rated higher, although the basic design is still the primary concern.
We need :
- A main page, with the rotating billboard and some other typical main page stuff
- 2 subpages with different formatted content blocks (1 column and 2 column)
This is a very short design contest, since we intend to go live very soon. Decision will be made quickly.
PSD file is sufficient, but it must be easy to slice to HTML/CSS (but we'll do that part ourselves).
Target Market(s)
IT Professionals
Industry/Entity Type
Internet
Look and feel
Each slider illustrates characteristics of the customer's brand and the style your logo design should communicate.

```html
<!DOCTYPE html>
<html lang="en">
<head>
<meta charset="utf-8">
<title>Brelvo – Home</title>
<link rel="stylesheet" href="https://fonts.googleapis.com/css2?family=Open+Sans:wght@400;600;700;800&display=swap">
<style>
  :root {
    --page-bg: #f0efe7;
    --panel-bg: #ffffff;
    --rule: #e6e5de;
    --text: #555555;
    --heading: #5a5a58;
    --nav: #5f5f5d;
    --accent: #e3222b;
    --brand: #2b2b2b;
    --brand-dot: #1c6ea4;
    --frame-bg: #f9f9f9;
    --frame-edge: #d9d9d9;
  }
  * { box-sizing: border-box; margin: 0; padding: 0; }
  html, body {
    width: 1200px; height: 522px; overflow: hidden;
    background: var(--page-bg);
    font-family: "Open Sans", Arial, sans-serif;
    color: var(--text);
  }
  .site { position: relative; width: 1200px; height: 522px; }

  .brand {
    position: absolute; left: 155px; top: 38px;
    display: flex; align-items: center; gap: 14px;
    font-weight: 800; font-size: 62px; line-height: 80px;
    color: var(--brand); letter-spacing: -2px;
  }
  .brand-dot { width: 22px; height: 22px; border-radius: 50%; background: var(--brand-dot); }

  .main-nav {
    position: absolute; right: 118px; top: 67px;
    display: flex; gap: 17px;
    font-weight: 700; font-size: 14px; text-transform: uppercase;
  }
  .main-nav a { color: var(--nav); text-decoration: none; }
  .main-nav a.login { color: var(--accent); }

  .panel {
    position: absolute; left: 123px; top: 170px; width: 960px; height: 400px;
    background: var(--panel-bg);
    box-shadow: 0 0 3px rgba(0,0,0,0.08);
  }
  .content { position: absolute; left: 46px; top: 37px; width: 540px; }
  .sidebar {
    position: absolute; left: 640px; top: 0; bottom: 0; width: 320px;
    border-left: 1px solid var(--rule);
    padding: 48px 10px 0 49px;
  }

  .billboard { position: relative; width: 538px; height: 180px; }
  .billboard-shadow {
    position: absolute; left: 4px; right: 4px; top: 140px; height: 34px;
    border-radius: 0 0 50% 50% / 0 0 30% 30%;
    box-shadow: 0 8px 6px -4px rgba(0,0,0,0.45);
  }
  .billboard-frame {
    position: absolute; inset: 0 0 24px 0;
    background: var(--frame-bg);
    border: 1px solid var(--frame-edge);
    border-radius: 8px;
    box-shadow: inset 3px 3px 6px rgba(0,0,0,0.18), 0 1px 2px rgba(0,0,0,0.15);
  }
  .billboard-controls {
    position: absolute; left: 218px; top: 138px; width: 100px; height: 42px;
    background: linear-gradient(#fdfdfd, #ececec);
    border: 1px solid #dcdcdc; border-radius: 6px;
    box-shadow: 0 2px 3px rgba(0,0,0,0.2);
  }

  .caption { font-size: 14px; line-height: 20px; margin-top: 4px; }
  .intro { font-size: 14px; line-height: 24px; margin-top: 11px; }

  .sidebar h3 {
    font-size: 13px; font-weight: 700; text-transform: uppercase;
    color: var(--heading); letter-spacing: -0.4px;
  }
  .about { display: flex; gap: 10px; margin-top: 14px; }
  .about-name {
    flex: 0 0 72px; margin-top: 14px;
    font-weight: 800; font-size: 17px; color: var(--brand); line-height: 20px;
  }
  .about p, .sidebar .blurb { font-size: 13px; line-height: 20px; }
  .sidebar .blurb { margin-top: 71px; width: 250px; }
</style>
</head>
<body>
<div class="site">
  <div class="brand"><span class="brand-dot"></span>brelvo</div>

  <nav class="main-nav">
    <a href="#">Home</a>
    <a href="#">Second page</a>
    <a href="#">Third page</a>
    <a href="#" class="login">Login</a>
  </nav>

  <div class="panel">
    <main class="content">
      <div class="billboard">
        <div class="billboard-shadow"></div>
        <div class="billboard-frame"></div>
        <div class="billboard-controls">
          <svg width="100" height="42" viewBox="0 0 100 42">
            <path d="M22 13 L15 21 L22 29" fill="none" stroke="#b5b5b5" stroke-width="3" stroke-linecap="round" stroke-linejoin="round"/>
            <path d="M78 13 L85 21 L78 29" fill="none" stroke="#b5b5b5" stroke-width="3" stroke-linecap="round" stroke-linejoin="round"/>
            <circle cx="49" cy="21" r="5" fill="#444"/>
          </svg>
        </div>
      </div>
      <p class="caption">The logo can be found at http://www.brelvo-link.example</p>
      <p class="intro">We’re looking for a clean and simple design, nothing super-fancy. There has to be room for some menu items and a place where people can login (so an e-mail and password box and login button, which must be replaced by the username and a logout button when the user is logged in).</p>
    </main>

    <aside class="sidebar">
      <h3>About Brelvo</h3>
      <div class="about">
        <span class="about-name">brelvo</span>
        <p>We're launching a brand new service which is designed to connect the current Internet Protocol (IPv4) to the new Internet Protocol (IPv6).</p>
      </div>
      <p class="blurb">Boolean prototype reducer transponder potentiometer logarithmic video, read-only transmission cache bus deviation deviation. Internet data developer for computer element device</p>
    </aside>
  </div>
</div>
</body>
</html>
```